Blog Webpage - Paw Harbour Ltd

Hello!!!!

Looking to incorporate a blog page on our current website www.pawharbour.co.uk. (Veterinary Recruitment Agency) The one we have is not very user friendly and is very limited in terms of what content can be added. Our current website is mainly word press, but if at all possible we would be looking for a HTML/Similar coded blog page to be added like our jobs page https://pawharbourjobs.brindlehire.com/ that seems to be picked up more by search engines.

Key Points:
1. Simple/user friendly, easy to update blog information I.e. updates from us, industry news, help/advice etc.
2. Updates to be added on a daily/weekly basis
3. Functionality’s like you have in a word document or similar – Front/Size/Colour etc.
4. Ease of upload/add written documents/images/graphics/vids etc.
5. Ability to easily amend/move content
6. Merge in with our current site/existing brand.
7. Ability to share on social media and mailers
8. SEO options
9. Add events
10. Manage customer comments
11. Ability for others to comment and for us to manage these
12. Possibly for these comments to be emailed to us, so we can pick them up ASAP?
13. Security and User login
14. Possibly page analytics
15. Like our FB, Twitter, Link, Google Plus pages etc
16. Ability to add competitions/surveys to be filled in

Many thanks for viewing this and hope someone can help!

Thanks Colin

Target Market(s)

Blog Webpage - Veterinary Recruitment Agency

Industry/Entity Type

Recruitment

Coding

Coded - Design and coding required

Font styles to use
Sans Serif

Colors
0555a3
9bcb3c

Requirements
Must have
• HTML/Similar
Nice to have
• As per brief

```html
<!DOCTYPE html>
<html lang="en">
<head>
<meta charset="utf-8">
<title>News &amp; Blogs – Paw Harbour</title>
<link href="https://fonts.googleapis.com/css2?family=Lato:wght@400;700&family=Gelasio:wght@400;700&family=Arimo:wght@400;700&display=swap" rel="stylesheet">
<style>
:root{
  --brand-blue:#0555a3;
  --brand-green:#9bcb3c;
  --navy:#1f3f70;
  --navy-field:#2c5594;
  --ink:#222;
  --body-text:#555;
  --muted:#8a8a8a;
  --rule:#dcdcdc;
  --page-bg:#e4e4e4;
  --footer:#2c2c2c;
  --footer-base:#1c1c1c;
  --heading-bar:#c4c4c4;
}
*{box-sizing:border-box;margin:0;padding:0}
html,body{width:1200px;height:2744px;overflow:hidden}
body{position:relative;background:var(--page-bg);font-family:"Lato",sans-serif;color:var(--ink)}
a{color:inherit;text-decoration:none}

/* header */
.site-header{position:absolute;left:0;top:0;width:1200px;height:137px;background:#fff;border-top:7px solid var(--brand-green);box-shadow:0 8px 18px rgba(0,0,0,.25);z-index:2}
.brand{position:absolute;left:86px;top:28px;display:flex;align-items:center;gap:12px}
.brand-mark{width:54px;height:54px;border-radius:50%;background:var(--brand-blue)}
.brand-name{font-family:"Lato",sans-serif;font-weight:700;font-size:36px;color:var(--brand-blue)}
.top-actions{position:absolute;left:602px;top:13px;display:flex;align-items:center;gap:6px}
.btn-top{background:#2f8fd6;color:#fff;font-size:15px;height:26px;line-height:26px;padding:0 11px}
.phone{font-family:"Arimo",sans-serif;font-size:27px;margin-left:8px;margin-right:8px;color:#111}
.social-squares{display:flex;gap:3px}
.social-squares span{display:block;width:27px;height:27px;background:var(--brand-blue)}
.header-email{position:absolute;right:88px;top:73px;font-size:16px;color:var(--brand-blue);display:flex;align-items:center;gap:5px}
.main-nav{position:absolute;right:86px;top:102px;display:flex;gap:2px;font-size:13px;color:#444}
.main-nav a{padding:5px 6px}
.main-nav a.is-current{background:var(--brand-green);color:#fff;border-radius:2px}

/* page */
.page{position:absolute;left:62px;top:139px;width:1076px;height:2334px;background:#fff}
.hero{position:absolute;left:0;top:0;width:1076px;height:424px;background:linear-gradient(180deg,#c8cde0 0%,#9aa3c6 45%,#6f78a6 100%)}
.breadcrumb{position:absolute;left:26px;top:449px;font-size:13px;color:#555}
.section-title{position:absolute;left:24px;top:492px;width:730px;height:40px;background:var(--heading-bar);font-family:"Gelasio",serif;font-weight:400;font-size:24px;line-height:40px;padding-left:13px;color:#222}

.post{position:absolute;left:24px;width:730px;height:375px}
.post-media{position:absolute;left:0;top:0;width:284px;height:329px}
.post-date{position:absolute;left:0;top:329px;width:284px;height:46px;background:var(--brand-green);font-family:"Arimo",sans-serif;font-size:16px;line-height:46px;text-align:center;color:#222;letter-spacing:.3px}
.post-body{position:absolute;left:315px;top:4px;width:392px}
.post-title{font-family:"Gelasio",serif;font-weight:400;font-size:31px;line-height:33px;color:#111;width:340px}
.post-excerpt{margin-top:24px;font-size:14.5px;line-height:22px;color:var(--body-text)}
.btn-more{position:absolute;top:229px;left:0;width:168px;height:46px;border:1px solid #aaa;font-size:13px;line-height:44px;text-align:center;color:#333}
.post-stats{position:absolute;left:320px;top:329px;font-size:11px;color:#777;display:flex;align-items:center;gap:4px;height:20px}
.share{position:absolute;left:428px;top:329px;display:flex;gap:7px}
.share span{width:20px;height:20px;border-radius:50%;background:#555}

.post--flip .post-media,.post--flip .post-date{left:448px}
.post--flip .post-body{left:25px;text-align:right}
.post--flip .post-title{margin-left:auto}
.post--flip .post-stats{left:165px}
.post--flip .share{left:272px}

/* sidebar */
.sidebar{position:absolute;left:803px;top:0;width:249px}
.job-alerts{position:absolute;top:454px;left:0;width:249px;height:217px;background:var(--navy);padding:14px 22px}
.job-alerts h3{font-family:"Gelasio",serif;font-size:18px;color:#fff;text-decoration:underline;margin-bottom:12px}
.job-alerts .field{height:25px;background:var(--navy-field);color:#b8c6de;font-size:10px;line-height:25px;padding-left:8px;margin-bottom:5px}
.job-alerts .btn-sub{display:inline-block;background:var(--navy-field);color:#fff;font-size:10px;padding:5px 8px;margin-top:2px}
.submit-cv{position:absolute;top:690px;left:0;width:249px;height:33px;background:var(--brand-green);border:2px solid #7aa52a;text-align:center;font-size:13px;line-height:29px;color:#2a3a10}
.latest-news{position:absolute;top:738px;left:0;width:249px}
.latest-news h3{font-size:24px;font-weight:400;margin-bottom:12px}
.news-item{height:55px;border-bottom:1px solid var(--rule);padding-top:6px}
.news-item p{font-size:11px;font-weight:700;color:#111}
.news-item a{font-size:9px;font-style:italic;color:var(--brand-green);font-weight:700}
.news-item:last-child{border:0}
.widget-head{height:39px;background:var(--navy);color:#fff;font-family:"Gelasio",serif;font-weight:700;font-size:15px;line-height:39px;padding-left:13px;letter-spacing:.5px}
.recent-posts{position:absolute;top:1086px;left:0;width:249px}
.recent-list{margin-top:18px}
.recent{display:flex;gap:25px;height:69px}
.recent .thumb{width:53px;height:36px;flex:none;margin-top:3px}
.recent h4{font-family:"Gelasio",serif;font-weight:400;font-size:13px;line-height:16px;color:#222;width:160px}
.recent time{font-family:"Gelasio",serif;font-size:10px;font-style:italic;color:#555;text-decoration:underline}
.tags{position:absolute;top:1507px;left:0;width:249px}
.tags ul{list-style:none;margin-top:6px}
.tags li{height:36px;line-height:36px;border-bottom:1px solid var(--rule);font-family:"Gelasio",serif;font-size:13px;padding-left:12px;color:#333}
.promo{position:absolute;top:1822px;left:0;width:249px;height:212px;background:linear-gradient(180deg,#e8e3d2 0%,#c9c6ad 45%,#6a7b3c 75%,#b0452c 100%)}

/* footer */
.site-footer{position:absolute;left:62px;top:2473px;width:1076px;height:225px;background:var(--footer);color:#fff}
.to-top{position:absolute;left:1030px;top:22px}
.foot-col{position:absolute;top:50px;list-style:none}
.foot-col li{font-size:13px;line-height:30px;letter-spacing:.4px}
.subscribe{position:absolute;left:774px;top:46px;width:278px}
.subscribe h4{font-size:13px;font-weight:400;letter-spacing:.5px}
.subscribe .email{margin-top:14px;height:33px;background:#e8e8e8;color:#999;font-size:13px;line-height:33px;padding-left:10px}
.subscribe .btn{position:absolute;right:0;top:79px;width:93px;height:34px;background:var(--brand-green);color:#222;font-size:12px;line-height:34px;text-align:center}
.foot-social{position:absolute;left:900px;top:170px;display:flex;gap:18px}
.foot-social span{width:16px;height:16px;border-radius:50%;background:#aaa}
.footer-base{position:absolute;left:62px;top:2698px;width:1076px;height:46px;background:var(--footer-base);color:#fff;font-size:13px;line-height:46px;padding:0 29px;display:flex;justify-content:space-between}
</style>
</head>
<body>

<header class="site-header">
  <a class="brand" href="#"><span class="brand-mark"></span><span class="brand-name">Paw Harbour</span></a>
  <div class="top-actions">
    <a class="btn-top" href="#">Register</a>
    <a class="btn-top" href="#">Timesheet Portal</a>
    <span class="phone">0300 555 0182</span>
    <div class="social-squares" aria-label="Social links"><span></span><span></span><span></span></div>
  </div>
  <a class="header-email" href="#">
    <svg width="15" height="11" viewBox="0 0 15 11"><rect x="0.5" y="0.5" width="14" height="10" fill="#222"/><path d="M1 1l6.5 5L14 1" stroke="#fff" fill="none"/></svg>
    info@pawharbour.co.uk
  </a>
  <nav class="main-nav">
    <a class="is-current" href="#">Home</a><a href="#">Job Seekers</a><a href="#">Clients</a><a href="#">Help &amp; Advice</a><a href="#">PH Loyalty Scheme</a><a href="#">News &amp; Blogs</a><a href="#">About Us</a><a href="#">Contact Us</a>
  </nav>
</header>

<div class="page">
  <div class="hero" role="img" aria-label="Businessman in a suit looking out over a city skyline with map pins showing candidate portraits"></div>
  <div class="breadcrumb">Home &gt; News &amp; Blogs</div>
  <h1 class="section-title">News &amp; Blogs</h1>

  <article class="post" style="top:565px">
    <div class="post-media" role="img" aria-label="Person in a yoga pose at sunset" style="background:linear-gradient(180deg,#d9a05c,#e9b46a 50%,#7a4a1e)"></div>
    <div class="post-date">JULY 1, 2015 &nbsp; | &nbsp; JANE DOE</div>
    <div class="post-body">
      <h2 class="post-title">This is the title of your first post</h2>
      <p class="post-excerpt">To create your first blog post, click here to open the Blog Manager. &nbsp;Edit your Published Post entitled 'This is the title of your first post', add your own text, images or videos, and click 'Publish'! From the Blog Manager you can also add a brand new post in a breeze…</p>
    </div>
    <a class="btn-more" href="#" style="left:315px">Continue Reading..</a>
    <div class="post-stats">4 <svg width="11" height="10" viewBox="0 0 11 10"><path d="M5.5 9L1.2 4.6A2.4 2.4 0 015.5 1.8a2.4 2.4 0 014.3 2.8z" fill="none" stroke="#777"/></svg> 25 <svg width="10" height="10" viewBox="0 0 10 10"><path d="M5 1C2.5 1 1 2.5 1 4.3c0 1 .5 1.8 1.3 2.3L2 9l2.4-1.5H5c2.5 0 4-1.5 4-3.2S7.5 1 5 1z" fill="none" stroke="#777"/></svg></div>
    <div class="share"><span></span><span></span><span></span><span></span><span></span></div>
  </article>

  <article class="post post--flip" style="top:1013px">
    <div class="post-media" role="img" aria-label="Tourist posing by a leaning stone tower" style="background:linear-gradient(180deg,#dfe3e8,#c9c2b0 60%,#5b5148)"></div>
    <div class="post-date">JULY 1, 2015 &nbsp; | &nbsp; JANE DOE</div>
    <div class="post-body">
      <h2 class="post-title">This is the title of your first post</h2>
      <p class="post-excerpt">To create your first blog post, click here to open the Blog Manager. &nbsp;Edit your Published Post entitled 'This is the title of your first post', add your own text, images or videos, and click 'Publish'! From the Blog Manager you can also add a brand new post in a breeze…</p>
    </div>
    <a class="btn-more" href="#" style="left:249px">Continue Reading..</a>
    <div class="post-stats">4 <svg width="11" height="10" viewBox="0 0 11 10"><path d="M5.5 9L1.2 4.6A2.4 2.4 0 015.5 1.8a2.4 2.4 0 014.3 2.8z" fill="none" stroke="#777"/></svg> 25 <svg width="10" height="10" viewBox="0 0 10 10"><path d="M5 1C2.5 1 1 2.5 1 4.3c0 1 .5 1.8 1.3 2.3L2 9l2.4-1.5H5c2.5 0 4-1.5 4-3.2S7.5 1 5 1z" fill="none" stroke="#777"/></svg></div>
    <div class="share"><span></span><span></span><span></span><span></span><span></span></div>
  </article>

  <article class="post" style="top:1458px">
    <div class="post-media" role="img" aria-label="Bowl of vegetable soup on a linen cloth" style="background:linear-gradient(180deg,#ece7dc,#a9b56a 55%,#e3e0d6)"></div>
    <div class="post-date">JULY 1, 2015 &nbsp; | &nbsp; JANE DOE</div>
    <div class="post-body">
      <h2 class="post-title">This is the title of your first post</h2>
      <p class="post-excerpt">To create your first blog post, click here to open the Blog Manager. &nbsp;Edit your Published Post entitled 'This is the title of your first post', add your own text, images or videos, and click 'Publish'! From the Blog Manager you can also add a brand new post in a breeze…</p>
    </div>
    <a class="btn-more" href="#" style="left:315px">Continue Reading..</a>
    <div class="post-stats">4 <svg width="11" height="10" viewBox="0 0 11 10"><path d="M5.5 9L1.2 4.6A2.4 2.4 0 015.5 1.8a2.4 2.4 0 014.3 2.8z" fill="none" stroke="#777"/></svg> 25 <svg width="10" height="10" viewBox="0 0 10 10"><path d="M5 1C2.5 1 1 2.5 1 4.3c0 1 .5 1.8 1.3 2.3L2 9l2.4-1.5H5c2.5 0 4-1.5 4-3.2S7.5 1 5 1z" fill="none" stroke="#777"/></svg></div>
    <div class="share"><span></span><span></span><span></span><span></span><span></span></div>
  </article>

  <article class="post post--flip" style="top:1897px">
    <div class="post-media" role="img" aria-label="Close-up of a colourful salad with sprouts" style="background:linear-gradient(180deg,#8fae5a,#d8794a 50%,#c8553a)"></div>
    <div class="post-date">JULY 1, 2015 &nbsp; | &nbsp; JANE DOE</div>
    <div class="post-body">
      <h2 class="post-title">This is the title of your first post</h2>
      <p class="post-excerpt">To create your first blog post, click here to open the Blog Manager. &nbsp;Edit your Published Post entitled 'This is the title of your first post', add your own text, images or videos, and click 'Publish'! From the Blog Manager you can also add a brand new post in a breeze…</p>
    </div>
    <a class="btn-more" href="#" style="left:249px">Continue Reading..</a>
    <div class="post-stats">4 <svg width="11" height="10" viewBox="0 0 11 10"><path d="M5.5 9L1.2 4.6A2.4 2.4 0 015.5 1.8a2.4 2.4 0 014.3 2.8z" fill="none" stroke="#777"/></svg> 25 <svg width="10" height="10" viewBox="0 0 10 10"><path d="M5 1C2.5 1 1 2.5 1 4.3c0 1 .5 1.8 1.3 2.3L2 9l2.4-1.5H5c2.5 0 4-1.5 4-3.2S7.5 1 5 1z" fill="none" stroke="#777"/></svg></div>
    <div class="share"><span></span><span></span><span></span><span></span><span></span></div>
  </article>

  <aside class="sidebar">
    <form class="job-alerts">
      <h3>JOB ALERTS</h3>
      <div class="field">Your Name</div>
      <div class="field">Your Email</div>
      <div class="field">Job Sector</div>
      <div class="field">Job Location</div>
      <span class="btn-sub">Subscribe now</span>
    </form>
    <a class="submit-cv" href="#">Submit Your CV</a>

    <section class="latest-news">
      <h3>Latest News</h3>
      <div class="news-item"><p>Waiter, there's a FLY in my…</p><a href="#">Read More</a></div>
      <div class="news-item"><p>WARNING! YUCKY PHOTOS!</p><a href="#">Read More</a></div>
      <div class="news-item"><p>Hare today(not) gone tomorrow</p><a href="#">Read More</a></div>
      <div class="news-item"><p>Asking the boss for a pay raise</p><a href="#">Read More</a></div>
      <div class="news-item"><p>The Quills</p><a href="#">Read More</a></div>
    </section>

    <section class="recent-posts">
      <h3 class="widget-head">RECENT POSTS</h3>
      <div class="recent-list">
        <div class="recent"><div class="thumb" role="img" aria-label="Sunset over water" style="background:linear-gradient(#e9b26e,#7d6a7a)"></div><div><h4>A CEO's Guide to Strate-gic Growth</h4><time>March 30, 2016</time></div></div>
        <div class="recent"><div class="thumb" role="img" aria-label="Video still of a meeting" style="background:linear-gradient(#3a3a3a,#6a6a6a)"></div><div><h4>Business Tip: How to Poll Clients</h4><time>March 30, 2016</time></div></div>
        <div class="recent"><div class="thumb" role="img" aria-label="Dusk landscape" style="background:linear-gradient(#6a5a7a,#c98a6a)"></div><div><h4>10 Essentials for the Traveling Businessman</h4><time>March 30, 2016</time></div></div>
        <div class="recent"><div class="thumb" role="img" aria-label="Sunset over water" style="background:linear-gradient(#e9b26e,#7d6a7a)"></div><div><h4>Review of the Harlow Report</h4><time>March 30, 2016</time></div></div>
        <div class="recent"><div class="thumb" role="img" aria-label="Video still of an interview" style="background:linear-gradient(#3a3a3a,#6a6a6a)"></div><div><h4>Profile: Tech Investor Tom Ridley</h4><time>March 29, 2016</time></div></div>
      </div>
    </section>

    <section class="tags">
      <h3 class="widget-head">SEARCH BY TAGS</h3>
      <ul><li>August 2016</li><li>July 2016</li><li>June 2016</li><li>May 2016</li><li>April 2016</li><li>Tags</li></ul>
    </section>

    <div class="promo" role="img" aria-label="Cookbook advert for Fresh Green Kitchen with a plated vegetable dish"></div>
  </aside>
</div>

<footer class="site-footer">
  <svg class="to-top" width="20" height="12" viewBox="0 0 20 12"><path d="M2 10l8-7 8 7" stroke="#ccc" stroke-width="3" fill="none"/></svg>
  <ul class="foot-col" style="left:61px"><li>HOME</li><li>ABOUT US/PAW HARBOUR</li><li>OUR SERVICE</li><li>TESTIMONIALS</li><li>DOWNLOADS/USEFUL LINKS</li></ul>
  <ul class="foot-col" style="left:313px"><li>MEET THE TEAM</li><li>VISION</li><li>WORK FOR US</li><li>REGISTER A VACANCY</li><li>ENQUIRY</li></ul>
  <ul class="foot-col" style="left:510px"><li>LOOKING FOR STAFF</li><li>CONTACT</li><li>OFFERS/COMPETITION</li><li>NEWS/BLOGS</li><li>JOB SEEKERS</li></ul>
  <div class="subscribe">
    <h4>SUBSCRIBE</h4>
    <div class="email">Enter Your Email</div>
    <span class="btn">SUBSCRIBE</span>
  </div>
  <div class="foot-social" aria-label="Social links"><span></span><span></span><span></span><span></span></div>
</footer>
<div class="footer-base">
  <span>© Copyright 2016 All rights reserved. &nbsp; | &nbsp; Paw Harbour</span>
  <span>Terms and Conditions &nbsp; | &nbsp; Privacy Policy</span>
</div>

</body>
</html>
```